Webdesign für  Photovoltaikanlagen und E-Ladeinfrastruktur
Webdesign für Photovoltaikanlagen und E-Ladeinfrastruktur
Zielgruppe
Die VALMO Energy GmbH ist ein Spezialist für die Planung und Projektierung von Photovoltaikanlagen und E-Ladeinfrastruktur.
Aufgabenstellung
- Design-Tool: Adobe Photoshop
- Hinweis: Die Firma wird sich neue aufstellen, was das Leistungsangebot betrifft. Sie können sich deshalb nur bedingt an der derzeitigen Website orientieren, alle fremden Logos (wie z.b. ORUPA) dürfen nicht mehr genutzt werden
- Gern hätten wir einen 'frischen' Slogan im headerbild

```html
<!DOCTYPE html>
<html lang="de">
<head>
<meta charset="utf-8">
<title>VALMO Energy GmbH</title>
<link href="https://fonts.googleapis.com/css2?family=Montserrat:wght@600;700&family=Arimo:wght@400;700&display=swap" rel="stylesheet">
<style>
:root{
  --green:#00774f;
  --text:#111;
  --grey-bg:#e6e6e6;
  --white:#fff;
  --line:#4aa784;
  --map-a:#eef0f2;
  --map-b:#e9ebe6;
}
*{margin:0;padding:0;box-sizing:border-box}
html,body{width:1200px;height:2804px;overflow:hidden;background:var(--white)}
body{position:relative;font-family:"Arimo",Arial,sans-serif;color:var(--text)}
.abs{position:absolute}
.brand{font-family:"Montserrat",sans-serif;font-weight:700;color:var(--green);letter-spacing:1px;white-space:nowrap}
.topline{left:100px;top:0;width:1000px;height:1px;background:#bbb}
.header-brand{left:50px;top:34px;font-size:28px}
.nav{right:45px;top:44px;display:flex;gap:25px;font-size:9.5px;letter-spacing:.2px}
.hero-panel{left:0;top:100px;width:600px;height:355px;background:var(--green)}
.hero-photo{left:600px;top:100px;width:600px;height:355px;background:linear-gradient(135deg,#cfe6fb 0%,#6fa7e6 35%,#2a5cc0 70%,#1c3f95 100%)}
.hero-title{left:111px;top:195px;font-family:"Montserrat",sans-serif;font-weight:700;font-size:24px;line-height:35px;color:var(--white);letter-spacing:.3px}
.btn-outline{border:3px solid var(--white);border-radius:30px;color:var(--white);font-family:"Montserrat",sans-serif;font-weight:600;display:flex;align-items:center;justify-content:center;letter-spacing:1px}
.hero-btn{left:108px;top:329px;width:176px;height:44px;font-size:20px}
.welcome-brand{left:200px;top:540px;font-size:30px;line-height:34px}
.welcome{left:400px;top:539px;width:540px;font-size:12.2px;line-height:14.5px}
.welcome h1{font-family:"Montserrat",sans-serif;font-size:13px;color:var(--green);font-weight:700;margin-bottom:12px}
.welcome h2{font-size:12.2px;font-weight:700;margin-bottom:11px}
.welcome ul{list-style:none}
.welcome li{position:relative;padding-left:10px;margin-bottom:11px}
.welcome li::before{content:"·";position:absolute;left:0;font-weight:700}
.btn-solid{background:var(--green);color:var(--white);border-radius:30px;font-family:"Montserrat",sans-serif;font-weight:700;display:flex;align-items:center;justify-content:center;letter-spacing:1.5px}
.welcome-btn{left:400px;top:794px;width:200px;height:41px;font-size:18px}
.svc{top:903px;width:400px;height:267px}
.svc-1{left:0;background:linear-gradient(180deg,#9fc5ec 0%,#b9cf6b 45%,#c8b260 60%,#8b8b8b 80%,#6a6a6a 100%)}
.svc-2{left:400px;background:linear-gradient(180deg,#a9c9ef 0%,#b65e35 40%,#3a5bab 55%,#f0f0ee 75%,#5a8a2a 100%)}
.svc-3{left:800px;background:linear-gradient(135deg,#1d4e33 0%,#c58b6d 45%,#2b3e6e 75%,#1e2d55 100%)}
.svc-band{left:0;top:1170px;width:1200px;height:77px;background:var(--green)}
.svc-btn{top:1191px;height:36px;font-size:13px;font-family:"Arimo",sans-serif;font-weight:700}
.news-bg{left:0;top:1247px;width:1200px;height:685px;background:var(--grey-bg)}
.section-title{font-family:"Montserrat",sans-serif;font-weight:700;font-size:18px;color:var(--green);letter-spacing:1px;width:1200px;text-align:center;left:0}
.card{top:1358px;width:234px;height:456px;background:var(--white);border:1px solid #9a9a9a}
.card-img{height:156px;border-bottom:1px solid #9a9a9a}
.card-body{padding:24px 36px 0 19px;font-size:12.4px;line-height:16px;color:var(--text)}
.card-body h3{font-size:13px;font-weight:700;margin-bottom:13px}
.card-body .more{color:var(--green);font-weight:700;margin-top:14px;display:block}
.news-btn{left:534px;top:1857px;width:139px;height:32px;font-size:13px;font-family:"Arimo",sans-serif}
.field{left:300px;width:600px;border-bottom:1px solid var(--line);color:var(--green);font-size:13.5px;padding-left:22px}
.send-btn{left:737px;top:2403px;width:151px;height:40px;font-size:18px}
.map{left:0;top:2499px;width:1200px;height:254px;background:linear-gradient(160deg,var(--map-a) 0%,var(--map-b) 100%)}
.footer{left:0;top:2753px;width:1200px;height:51px;background:var(--green);color:var(--white);font-size:9.5px}
.footer span{position:absolute;top:19px}
</style>
</head>
<body>
<div class="abs topline"></div>
<div class="abs brand header-brand">VALMO ENERGY</div>
<nav class="abs nav">
  <span>UNTERNEHMENEN</span><span>E-LADEINFRASTRUKTUR</span><span>PHOTOVOLTAIK</span><span>PLANUNG UND PROJEKTIERUNG</span><span>AKTUELLES</span><span>KONTAKT</span>
</nav>

<div class="abs hero-panel"></div>
<div class="abs hero-photo" role="img" aria-label="Solarmodule unter blauem Himmel mit Sonne"></div>
<h1 class="abs hero-title">IHR SPEZIALIST FÜR ANLAGEN<br>DER REGENERATIVEN<br>ENERGIEERZEUGUNG</h1>
<div class="abs btn-outline hero-btn">KONTAKT</div>

<div class="abs brand welcome-brand">VALMO<br>ENERGY</div>
<section class="abs welcome">
  <h1>HERZLICH WILLKOMMEN AUF DEN SEITEN DER VALMO ENERGY GMBH</h1>
  <h2>Ihrem Spezialist für:</h2>
  <ul>
    <li>Planung und Realisierung von Photovoltaikanlagen und Solartrackern zur Dach- oder Freilandmontage,</li>
    <li>Entwicklung, Fertigung und Vertrieb von vertikalachsigen Windenergieanlagen,</li>
    <li>Reparatur und Überholung von Windkraftgetrieben bis 2,5 Megawatt Nennleistung,</li>
    <li>Sanierung und Automatisierung von Wasserkraftwerken bis ein Megawatt Nennleistung,</li>
    <li>Strahlen und Beschichten von Bauteilen bis 22 m Länge und 25 t Stückgewicht,</li>
    <li>Herstellung und Regenerierung von Bauteilen und Komponenten im Verbund mit der KRALO Werkstofftechnik GmbH.</li>
  </ul>
</section>
<div class="abs btn-solid welcome-btn">UNTERNEHMEN</div>

<div class="abs svc svc-1" role="img" aria-label="Elektroauto an Ladesäule vor einem Feld"></div>
<div class="abs svc svc-2" role="img" aria-label="Wohnhaus mit Solaranlage auf dem Dach"></div>
<div class="abs svc svc-3" role="img" aria-label="Hände halten eine junge Pflanze"></div>
<div class="abs svc-band"></div>
<div class="abs btn-outline svc-btn" style="left:85px;width:230px">E-LADEINFRASTRUKTUR</div>
<div class="abs btn-outline svc-btn" style="left:515px;width:170px">PHOTOVOLTAIK</div>
<div class="abs btn-outline svc-btn" style="left:865px;width:270px">PLANUNG UND PROJEKTIERUNG</div>

<div class="abs news-bg"></div>
<h2 class="abs section-title" style="top:1302px">AKTUELLES</h2>
<article class="abs card" style="left:200px">
  <div class="card-img" role="img" aria-label="Windkraftanlage über Wald und Wiesen" style="background:linear-gradient(180deg,#7fb0e0 0%,#cfe0f0 45%,#4f7a33 70%,#2e4a20 100%)"></div>
  <div class="card-body"><h3>Beltrag Lorem Ipsum</h3><p>Lorem ipsum dolor sit amet, consetetur sadipscing elitr, sed diam nonumy eirmod tempor invidunt ut labore et dolore magna aliquyam erat, sed diam voluptua. At vero eos et accusam et justo duo dolores et ea rebum. Stet clita kasd gubergren, no sea takimata sanctus est Lorem ipsum dolor sit amet…</p><span class="more">mehr...</span></div>
</article>
<article class="abs card" style="left:482px">
  <div class="card-img" role="img" aria-label="Rohrleitungen einer Industrieanlage" style="background:linear-gradient(135deg,#1e5fae 0%,#2a9c74 45%,#c9d3de 70%,#1b3f7a 100%)"></div>
  <div class="card-body"><h3>Beltrag Lorem Ipsum</h3><p>Lorem ipsum dolor sit amet, consetetur sadipscing elitr, sed diam nonumy eirmod tempor invidunt ut labore et dolore magna aliquyam erat, sed diam voluptua. At vero eos et accusam et justo duo dolores et ea rebum. Stet clita kasd gubergren, no sea takimata sanctus est Lorem ipsum dolor sit amet…</p><span class="more">mehr...</span></div>
</article>
<article class="abs card" style="left:766px">
  <div class="card-img" role="img" aria-label="Monteure installieren Solarmodule auf einem Dach" style="background:linear-gradient(135deg,#8c6a5a 0%,#2c3f7c 45%,#1f2d5e 100%)"></div>
  <div class="card-body"><h3>Beltrag Lorem Ipsum</h3><p>Lorem ipsum dolor sit amet, consetetur sadipscing elitr, sed diam nonumy eirmod tempor invidunt ut labore et dolore magna aliquyam erat, sed diam voluptua. At vero eos et accusam et justo duo dolores et ea rebum. Stet clita kasd gubergren, no sea takimata sanctus est Lorem ipsum dolor sit amet…</p><span class="more">mehr...</span></div>
</article>
<div class="abs btn-solid news-btn">SIEHE MEHR</div>

<h2 class="abs section-title" style="top:1993px">KONTAKFORMULAR</h2>
<div class="abs field" style="top:2050px;height:26px">Name / Firma</div>
<div class="abs field" style="top:2106px;height:28px">Telefon</div>
<div class="abs field" style="top:2162px;height:29px">E-Mail</div>
<div class="abs field" style="top:2218px;height:32px">Ansprechpartner</div>
<div class="abs field" style="top:2274px;height:99px">Nachricht</div>
<div class="abs btn-solid send-btn">SENDEN</div>

<div class="abs map" role="img" aria-label="Karte mit Standort des Unternehmens"></div>
<footer class="abs footer"><span style="left:203px">Impressum</span><span style="left:274px">Datenschutz</span></footer>
</body>
</html>
```